Business Card & Word Docs from existing Logo

We need a business card with typical information plus layout to include electrical contractors license number, VORLE license and KMT license. We would like a word document layout for a proposal document, opening page with logo and design basic information; proposal to and proposal from and project name and number. Small basic single page letter for general documents. Email signature with logo.

We are an electrical, refrigeration and automation contractor. We work with reducing energy consumption for our customers and complex process solutions in electrical, refrigeration and automation.
Updates

Reason: Final changes/ revisions to designs.

Target Market(s)

Industrial and commercial businesses that require more than your average contractor.

Industry/Entity Type

Electrical

Requirements
Must have
• Propsal document must have a full opening page.

```html
<!DOCTYPE html>
<html lang="en">
<head>
<meta charset="utf-8">
<title>Frostline Contracting – Business Card</title>
<link rel="stylesheet" href="https://fonts.googleapis.com/css2?family=Open+Sans:wght@400;600;700&display=swap">
<style>
  :root {
    --page: #e9eaec;
    --card-white: #ffffff;
    --brand-blue: #1c7fb4;
    --brand-green: #17924f;
    --navy: #1d3b6a;
    --ink: #2a2a2a;
    --ghost: #f0f0f0;
    --back-circle: #1a82b5;
  }
  * { box-sizing: border-box; margin: 0; padding: 0; }
  html, body { width: 1200px; height: 900px; overflow: hidden; }
  body {
    background: var(--page);
    font-family: "Open Sans", Arial, sans-serif;
    position: relative;
  }
  .card {
    position: absolute;
    top: 307px;
    width: 502px;
    height: 288px;
    border-radius: 16px;
    overflow: hidden;
    box-shadow: 0 2px 6px rgba(0,0,0,0.18);
  }
  .card--front { left: 77px; background: var(--card-white); }
  .card--back {
    left: 622px;
    background: linear-gradient(180deg, var(--brand-green) 0%, #178a78 45%, var(--brand-blue) 100%);
  }
  .ghost-circle {
    position: absolute;
    border-radius: 50%;
  }
  .card--front .ghost-circle {
    width: 370px; height: 370px; left: 70px; top: 26px;
    background: var(--ghost);
  }
  .card--back .ghost-circle {
    width: 376px; height: 376px; left: 63px; top: 28px;
    background: var(--back-circle);
  }
  .brand {
    position: absolute;
    display: flex;
    align-items: center;
    gap: 10px;
  }
  .brand__dot { border-radius: 50%; flex: none; }
  .brand__name { font-weight: 700; line-height: 1; }
  .brand__name span { display: block; }
  .card--front .brand { right: 36px; top: 28px; }
  .card--front .brand__dot { width: 38px; height: 38px; background: var(--brand-blue); }
  .card--front .brand__name { color: var(--brand-blue); }
  .card--front .brand__main { font-size: 27px; letter-spacing: -0.5px; }
  .card--front .brand__sub { font-size: 15px; letter-spacing: 4.6px; margin-top: 4px; }

  .card--back .brand {
    left: 0; right: 0; top: 60px;
    flex-direction: column;
    gap: 14px;
  }
  .card--back .brand__dot { width: 70px; height: 70px; background: #ffffff; }
  .card--back .brand__name { color: #ffffff; text-align: center; }
  .card--back .brand__main { font-size: 36px; letter-spacing: -0.5px; }
  .card--back .brand__sub { font-size: 18px; letter-spacing: 8px; margin-top: 8px; }
  .card--back .web {
    position: absolute; left: 0; right: 0; top: 261px;
    text-align: center; color: #ffffff;
    font-size: 10.5px; letter-spacing: 2px;
  }

  .person { position: absolute; left: 27px; top: 98px; color: var(--navy); }
  .person__name { font-weight: 700; font-size: 14px; line-height: 18px; }
  .person__role { font-size: 14px; line-height: 18px; }
  .address {
    position: absolute; left: 27px; top: 151px;
    font-size: 12px; color: var(--ink);
  }
  .contacts {
    position: absolute; left: 27px; top: 173px;
    list-style: none; font-size: 12px; color: var(--ink);
  }
  .contacts li { display: flex; align-items: center; gap: 5px; height: 17px; }
  .contacts svg { width: 12px; height: 12px; fill: var(--navy); flex: none; }
  .licences {
    position: absolute; right: 30px; top: 270px;
    display: flex; font-size: 8.5px; color: var(--ink);
  }
  .licences span + span { border-left: 1px solid var(--ink); margin-left: 5px; padding-left: 5px; }
</style>
</head>
<body>
  <section class="card card--front" aria-label="Business card front">
    <div class="ghost-circle"></div>
    <div class="brand">
      <div class="brand__dot"></div>
      <div class="brand__name"><span class="brand__main">FROSTLINE</span><span class="brand__sub">CONTRACTING</span></div>
    </div>
    <div class="person">
      <p class="person__name">Daniel Harrow</p>
      <p class="person__role">Director</p>
    </div>
    <p class="address">PO Box 5820, Mossvale, Queensland, 4999</p>
    <ul class="contacts">
      <li><svg viewBox="0 0 12 12"><path d="M1 4c0-2 2-3 5-3s5 1 5 3l-2 1-1-2H4L3 5zM3 6h6l2 5H1z"/></svg>07 5550 2810</li>
      <li><svg viewBox="0 0 12 12"><path d="M3 1h6v3H3zM1 5h10v5H9V8H3v2H1zM3 9h6v2H3z"/></svg>07 5550 2811</li>
      <li><svg viewBox="0 0 12 12"><path d="M3.5 0.5h5v11h-5zM4.5 2v6h3V2z"/></svg>0400 555 918</li>
      <li><svg viewBox="0 0 12 12"><path d="M0.5 2.5h11v7h-11zM1.5 3.5v0.4l4.5 3 4.5-3v-0.4zM1.5 5v3.5h9V5L6 8z"/></svg>daniel@frostline.com.au</li>
      <li><svg viewBox="0 0 12 12"><path d="M6 0.5a5.5 5.5 0 1 0 0 11a5.5 5.5 0 1 0 0-11zM1.6 5.4h2.2c0-1.6.4-2.9 1-3.7A4.5 4.5 0 0 0 1.6 5.4zM4.8 5.4h2.4C7.1 3.6 6.6 2 6 1.6 5.4 2 4.9 3.6 4.8 5.4zM8.2 5.4h2.2A4.5 4.5 0 0 0 7.2 1.7c.6.8 1 2.1 1 3.7zM1.6 6.6a4.5 4.5 0 0 0 3.2 3.7c-.6-.8-1-2.1-1-3.7zM4.8 6.6c.1 1.8.6 3.4 1.2 3.8.6-.4 1.1-2 1.2-3.8zM8.2 6.6c0 1.6-.4 2.9-1 3.7a4.5 4.5 0 0 0 3.2-3.7z"/></svg>www.frostline.com.au</li>
    </ul>
    <p class="licences"><span>Electrical Contractors License 12345</span><span>KMT 1234567</span><span>VORLE AA12345</span></p>
  </section>

  <section class="card card--back" aria-label="Business card back">
    <div class="ghost-circle"></div>
    <div class="brand">
      <div class="brand__dot"></div>
      <div class="brand__name"><span class="brand__main">FROSTLINE</span><span class="brand__sub">CONTRACTING</span></div>
    </div>
    <p class="web">www.frostline.com.au</p>
  </section>
</body>
</html>
```